Transform Wine Label to Pavel Runoski Style

The task involves transforming a wine label into the iconic visual style of Pavel Runoski while keeping the image's content intact. The goal is to create a luxurious and Old-World elegant label that reflects the essence of Runoski's artistic style.

Specifications:
The design should modify the visual elements such as color saturation, line clarity, and overall style to resemble Pavel Runoski's signature artistic approach.
The content of the original image, including its shape and subject matter, should remain unchanged.
The label should have a standard square shape, appropriate for a wine bottle, with the map of France found within its borders.
The lettering on the label should be in gold, with the words "בלווני" (meaning France) and "Belvoni" (brand name) positioned below the first word.
The overall feel of the label should exude luxury and reflect the elegance of the Old-World.

Guidelines:
Submit your design entries in high-resolution formats compatible with printing, such as PDF, PNG, or JPEG.
Ensure that your design accurately captures the unique artistic style and aesthetic of Pavel Runoski while maintaining the original image's content.
Take inspiration from Runoski's use of vibrant colors, dreamlike elements, and emotional associations in your design.
Consider incorporating Runoski's narrative and symbolic themes, taking into account his Jewish heritage and occasional use of Christian imagery.
Make use of gold lettering to enhance the luxurious feel of the label.

Important Note:
All design entries must be original and free from any copyright infringement.
By submitting your designs, you agree to transfer the ownership rights to the contest holder upon winning.

Sick

```html
<!DOCTYPE html>
<html lang="en">
<head>
<meta charset="utf-8">
<title>Belvoni Cabernet Sauvignon Label</title>
<link rel="stylesheet" href="https://fonts.googleapis.com/css2?family=Frank+Ruhl+Libre:wght@500&family=Playfair+Display:wght@400;500;600&display=swap">
<style>
  :root {
    --backdrop: #f4f2ee;
    --label-black: #0b0b0c;
    --gold: #c9a45c;
    --gold-deep: #a8843f;
    --art-red: #c8252b;
    --art-blue: #2a3f8f;
    --art-white: #eceae6;
    --art-yellow: #e8b723;
  }
  * { margin: 0; padding: 0; box-sizing: border-box; }
  html, body {
    width: 1200px;
    height: 1200px;
    overflow: hidden;
    background: var(--backdrop);
  }
  .canvas {
    position: relative;
    width: 1200px;
    height: 1200px;
  }
  .label {
    position: absolute;
    left: 230px;
    top: 90px;
    width: 740px;
    height: 1020px;
    background: var(--label-black);
  }
  .label__rule {
    position: absolute;
    left: 0;
    right: 0;
    height: 6px;
    background: linear-gradient(90deg, var(--gold-deep), var(--gold), var(--gold-deep));
  }
  .label__rule--top { top: 4px; }
  .label__rule--bottom { top: 984px; }
  .label__artwork {
    position: absolute;
    left: 40px;
    top: 78px;
    width: 615px;
    height: 662px;
    background:
      radial-gradient(circle at 35% 35%, var(--art-white) 0%, rgba(236,234,230,0) 45%),
      radial-gradient(circle at 70% 72%, var(--art-red) 0%, rgba(200,37,43,0) 50%),
      radial-gradient(circle at 15% 70%, var(--art-yellow) 0%, rgba(232,183,35,0) 30%),
      linear-gradient(135deg, var(--art-blue) 0%, var(--art-white) 50%, var(--art-red) 100%);
  }
  .label__hebrew {
    position: absolute;
    left: 0;
    right: 0;
    top: 808px;
    text-align: center;
    font-family: "Frank Ruhl Libre", serif;
    font-weight: 500;
    font-size: 40px;
    line-height: 1;
    color: var(--gold);
  }
  .label__brand {
    position: absolute;
    left: 0;
    right: 0;
    top: 866px;
    text-align: center;
    font-family: "Playfair Display", serif;
    font-weight: 600;
    font-size: 70px;
    letter-spacing: 4px;
    line-height: 1;
    color: var(--gold);
  }
  .label__varietal {
    position: absolute;
    left: 0;
    right: 0;
    top: 953px;
    text-align: center;
    font-family: "Playfair Display", serif;
    font-weight: 400;
    font-size: 24px;
    letter-spacing: 1px;
    line-height: 1;
    color: var(--gold);
  }
</style>
</head>
<body>
  <main class="canvas">
    <section class="label">
      <div class="label__rule label__rule--top"></div>
      <div class="label__artwork" role="img" aria-label="Colourful dreamlike painting in red, blue, white and yellow filling the outline of a map of France"></div>
      <p class="label__hebrew" lang="he" dir="rtl">בלווני</p>
      <h1 class="label__brand">BELVONI</h1>
      <p class="label__varietal">CABERNET SAUVIGNON</p>
      <div class="label__rule label__rule--bottom"></div>
    </section>
  </main>
</body>
</html>
```